Coffee Pouch Label for Coffee Roaster

We are wanting some new labels for our coffee pouches.
We are an established, small family owned specialty coffee roaster called Tarn4 Coffee Roasters, and we are located in Orrin, NSW Australia.
Label dimensions are 100 x 150mm, to fit on a couple of different bag sizes. We use coffee pouches with kraft paper finish.
We have 3 main blends, Lanternfly, Quillrock & Pale Finch, and a range of rotating single origin coffees. We would get labels printed for the blends, but then need a 'generic' design that we can either write the name on, or stick another sticker over for the single origin coffees.
Some information that needs to be on the label:
our logo
web address: www.tarn4coffee.example
address: 47 Corvell St, Orrin, NSW
Proudly Roasted in Orrin, NSW
Blend name
our tagline/mission: Roast slowly | Share freely | Give gladly
statement: We give $1 from every kg of coffee sold to programs that keep young children safe, schooled and free from harm.
We would like to use colour to help differentiate the different blends somehow.
We are after a creative, clean design, that is representative of specialty coffee (not large commercial coffee brands).
I have uploaded our logo both with and without our tagline, and also some other packaging inspiration that i like (I quite like the meadow coffee label design).
thanks everyone!
Marcus
People who appreciate good, local coffee

```html
<!DOCTYPE html>
<html lang="en">
<head>
<meta charset="utf-8">
<title>Tarn4 Coffee Roasters — Pouch Labels</title>
<link rel="stylesheet" href="https://fonts.googleapis.com/css2?family=Bebas+Neue&family=Barlow+Semi+Condensed:wght@500;600;700&display=swap">
<style>
  :root {
    --page: #ffffff;
    --label: #ffffff;
    --ink: #1c1c1c;
    --on-band: #ffffff;
    --quillrock-a: #2e0604;
    --quillrock-b: #5e1006;
    --lanternfly-a: #5e3d22;
    --lanternfly-b: #ac7c4c;
    --palefinch-a: #262626;
    --palefinch-b: #3c3c3c;
    --generic-a: #0b2413;
    --generic-b: #1a3f24;
  }
  * { box-sizing: border-box; margin: 0; padding: 0; }
  html, body { width: 1200px; height: 640px; overflow: hidden; background: var(--page); }
  body { position: relative; font-family: "Barlow Semi Condensed", "Arial Narrow", sans-serif; color: var(--ink); }

  .label {
    position: absolute; top: 100px; width: 285px; height: 427px;
    background: var(--label); box-shadow: 0 0 3px rgba(0,0,0,.28);
  }
  .label--quillrock { left: 18px; --band-a: var(--quillrock-a); --band-b: var(--quillrock-b); }
  .label--lanternfly { left: 312px; --band-a: var(--lanternfly-a); --band-b: var(--lanternfly-b); }
  .label--palefinch { left: 606px; --band-a: var(--palefinch-a); --band-b: var(--palefinch-b); }
  .label--generic { left: 902px; --band-a: var(--generic-a); --band-b: var(--generic-b); }

  .band { position: absolute; inset: 0 0 auto 0; height: 179px; color: var(--on-band); }
  .band__texture { position: absolute; inset: 0; background: linear-gradient(120deg, var(--band-a), var(--band-b)); }

  .brand { position: absolute; left: 0; right: 0; top: 46px; text-align: center; font-weight: 700; color: var(--on-band); }
  .brand__name { display: block; font-size: 50px; line-height: 44px; letter-spacing: 1px; }
  .brand__sub { display: block; font-size: 9px; letter-spacing: 1.4px; margin-top: 2px; padding-left: 80px; }

  .tagline {
    position: absolute; top: 155px; left: 0; right: 0;
    display: flex; justify-content: center; align-items: center;
    font-size: 6.5px; font-weight: 600; letter-spacing: 1.2px;
  }
  .tagline span { padding: 0 11px; }
  .tagline span + span { border-left: 1.2px solid var(--on-band); }

  .blend-name {
    position: absolute; top: 214px; left: 0; right: 0; text-align: center;
    font-family: "Bebas Neue", "Arial Narrow", sans-serif; font-size: 46px; line-height: 46px; letter-spacing: 0.5px;
  }
  .rule-h { position: absolute; height: 1.2px; background: var(--ink); }
  .rule-v { position: absolute; width: 1.2px; background: var(--ink); }

  .tasting { position: absolute; top: 282px; left: 46px; font-size: 12.5px; font-weight: 600; }
  .origin {
    position: absolute; top: 280px; left: 166px; width: 80px; text-align: center;
    font-size: 7.5px; font-weight: 700; line-height: 8px; text-transform: uppercase;
  }
  .origin--generic { top: 198px; left: 102px; }

  .mission {
    position: absolute; left: 0; right: 0; text-align: center;
    font-size: 6.6px; font-weight: 500; line-height: 8.4px; text-transform: uppercase; letter-spacing: .2px;
  }
  .mission strong { font-weight: 700; }

  .footer { position: absolute; top: 384px; font-size: 5.6px; font-weight: 700; letter-spacing: .3px; }
  .footer--address { left: 46px; }
  .footer--web { left: 158px; letter-spacing: 1.2px; }
</style>
</head>
<body>

  <article class="label label--quillrock">
    <header class="band">
      <div class="band__texture" role="img" aria-label="Wave pattern on deep red gradient"></div>
      <div class="brand"><span class="brand__name">Tarn4</span><span class="brand__sub">COFFEE ROASTERS</span></div>
      <p class="tagline"><span>ROAST SLOWLY</span><span>SHARE FREELY</span><span>GIVE GLADLY</span></p>
    </header>
    <h2 class="blend-name">QUILLROCK</h2>
    <div class="rule-h" style="top:266px;left:98px;width:98px"></div>
    <div class="rule-v" style="top:266px;left:146px;height:45px"></div>
    <p class="tasting">Smooth &amp; Sweet</p>
    <p class="origin">Proudly roasted<br>in Orrin, NSW</p>
    <p class="mission" style="top:330px">We give <strong>$1</strong> from every kg of coffee sold<br>to <strong>programs that keep young children<br>safe, schooled and free from harm.</strong></p>
    <p class="footer footer--address">47 Corvell St, Orrin, NSW</p>
    <div class="rule-v" style="top:380px;left:146px;height:20px"></div>
    <p class="footer footer--web">www.tarn4coffee.example</p>
  </article>

  <article class="label label--lanternfly">
    <header class="band">
      <div class="band__texture" role="img" aria-label="Wave pattern on caramel brown gradient"></div>
      <div class="brand"><span class="brand__name">Tarn4</span><span class="brand__sub">COFFEE ROASTERS</span></div>
      <p class="tagline"><span>ROAST SLOWLY</span><span>SHARE FREELY</span><span>GIVE GLADLY</span></p>
    </header>
    <h2 class="blend-name">LANTERNFLY</h2>
    <div class="rule-h" style="top:266px;left:98px;width:98px"></div>
    <div class="rule-v" style="top:266px;left:146px;height:45px"></div>
    <p class="tasting">Smooth &amp; Sweet</p>
    <p class="origin">Proudly roasted<br>in Orrin, NSW</p>
    <p class="mission" style="top:330px">We give <strong>$1</strong> from every kg of coffee sold<br>to <strong>programs that keep young children<br>safe, schooled and free from harm.</strong></p>
    <p class="footer footer--address">47 Corvell St, Orrin, NSW</p>
    <div class="rule-v" style="top:380px;left:146px;height:20px"></div>
    <p class="footer footer--web">www.tarn4coffee.example</p>
  </article>

  <article class="label label--palefinch">
    <header class="band">
      <div class="band__texture" role="img" aria-label="Wave pattern on charcoal gradient"></div>
      <div class="brand"><span class="brand__name">Tarn4</span><span class="brand__sub">COFFEE ROASTERS</span></div>
      <p class="tagline"><span>ROAST SLOWLY</span><span>SHARE FREELY</span><span>GIVE GLADLY</span></p>
    </header>
    <h2 class="blend-name">PALE FINCH</h2>
    <div class="rule-h" style="top:266px;left:98px;width:98px"></div>
    <div class="rule-v" style="top:266px;left:146px;height:45px"></div>
    <p class="tasting">Smooth &amp; Sweet</p>
    <p class="origin">Proudly roasted<br>in Orrin, NSW</p>
    <p class="mission" style="top:330px">We give <strong>$1</strong> from every kg of coffee sold<br>to <strong>programs that keep young children<br>safe, schooled and free from harm.</strong></p>
    <p class="footer footer--address">47 Corvell St, Orrin, NSW</p>
    <div class="rule-v" style="top:380px;left:146px;height:20px"></div>
    <p class="footer footer--web">www.tarn4coffee.example</p>
  </article>

  <article class="label label--generic">
    <header class="band">
      <div class="band__texture" role="img" aria-label="Wave pattern on forest green gradient"></div>
      <div class="brand"><span class="brand__name">Tarn4</span><span class="brand__sub">COFFEE ROASTERS</span></div>
      <p class="tagline"><span>ROAST SLOWLY</span><span>SHARE FREELY</span><span>GIVE GLADLY</span></p>
    </header>
    <div class="rule-h" style="top:205px;left:58px;width:34px"></div>
    <p class="origin origin--generic">Proudly roasted<br>in Orrin, NSW</p>
    <div class="rule-h" style="top:205px;left:192px;width:34px"></div>
    <div class="rule-h" style="top:333px;left:92px;width:97px"></div>
    <p class="mission" style="top:343px">We give <strong>$1</strong> from every kg of coffee sold<br>to <strong>programs that keep young children<br>safe, schooled and free from harm.</strong></p>
    <p class="footer footer--address">47 Corvell St, Orrin, NSW</p>
    <div class="rule-v" style="top:380px;left:146px;height:20px"></div>
    <p class="footer footer--web">www.tarn4coffee.example</p>
  </article>

</body>
</html>
```